Termite Mailer September 2021

We need a clean modern looking flyer advertising termites via the mail.

Size should be 9"x6"

Our tagline is "The Smarter Approach to Pest Control"

Something along the stylistic design of these:

https://pics.hollowmarsh.example/Qa83LkTzWp

https://pics.hollowmarsh.example/Rn47VbXcMd

https://pics.hollowmarsh.example/Hj29PsYeUf

https://www.flintquillprint.example/wp-content/uploads/designs/img/Pest-Prevention-Postcard-PST-1003.jpg

Should include some of this verbiage:

HAVE YOU SCHEDULED YOUR ANNUAL TERMITE INSPECTION? - MAKE IT IN RED

DON'T WAIT. PROTECT YOUR HOME TODAY!

ABSOLUTELY FREE INSPECTION. NO OBLIGATION.

TERMITES CAN CAUSE SEVERE DAMAGE TO YOUR HOME.

BRINDLEVALE LOGO

THE SMARTER APPROACH TO PEST CONTROL.

PROTECT YOUR MOST VALUABLE ASSET.

10% DISCOUNT ON ANY SERVICE GUARANTEED IF YOU CALL TODAY.

INCLUDE A PICTURE OF A TERMITE AS WELL SOMEWHERE AND WOOD DAMAGE.

Target Market(s)

Homeowners in Southern California USA

Industry/Entity Type

Pest Control/Extermination

Font styles to use
Other font styles liked:
• Chaparral Pro Italic, Brava Slab

Requirements
Must have
• Clean design, picture of house, picture of Termite, 10% off coupon and call to action on the back
Should not have
• Bad looking houses, colors that don't match our logo

```html
<!DOCTYPE html>
<html lang="en">
<head>
<meta charset="utf-8">
<title>Brindlevale Termite Mailer</title>
<link href="https://fonts.googleapis.com/css2?family=Oswald:wght@500;700&family=Montserrat:wght@400;500;600;700;800&display=swap" rel="stylesheet">
<style>
  :root{
    --green:#6cbf2c;
    --green-dark:#4f9a1e;
    --blue:#1565b8;
    --blue-deep:#0b4c8c;
    --red:#c0141b;
    --charcoal:#555557;
    --ink:#3b3b3b;
    --white:#ffffff;
    --stamp:#e0e0e0;
  }
  *{margin:0;padding:0;box-sizing:border-box}
  html,body{width:1200px;height:1200px;overflow:hidden;background:var(--white)}
  body{position:relative;font-family:'Montserrat',sans-serif}
  .card{position:absolute;left:235px;width:738px;height:492px;overflow:hidden;box-shadow:0 6px 16px rgba(0,0,0,.28);background:var(--white)}
  .card--front{top:81px}
  .card--back{top:634px}
  .abs{position:absolute}

  .brand{display:flex;align-items:center;gap:8px}
  .brand__mark{width:20px;height:20px;background:var(--green)}
  .brand__name{font-family:'Montserrat',sans-serif;font-weight:700;color:var(--ink);font-size:21px;line-height:1;letter-spacing:.5px}
  .tagline{font-family:'Montserrat',sans-serif;font-weight:500;color:var(--blue);font-size:11px;letter-spacing:.2px}

  .headline{font-family:'Oswald',sans-serif;font-weight:700;line-height:1;text-transform:uppercase}
  .headline--green{color:var(--green);font-size:38px}
  .headline--grey{color:var(--ink);font-size:23px;font-weight:500}
  .headline--red{color:var(--red);font-size:31px}
  .subhead{color:var(--blue);font-weight:800;font-size:11.5px;text-transform:uppercase}

  .photo-house{left:0;top:0;width:738px;height:400px}
  .insects{left:14px;top:212px;width:300px;height:108px;border-radius:40px;background:radial-gradient(ellipse at 65% 55%,#c46a32 0%,#e6b98a 30%,rgba(255,255,255,0) 70%)}

  .offer-band{left:0;top:334px;width:560px;height:57px;background:linear-gradient(90deg,var(--green-dark) 0%,var(--green) 60%,rgba(108,191,44,.4) 100%)}
  .offer-band p{position:absolute;left:20px;font-size:13px;color:#22301a;white-space:nowrap}
  .offer-band b{font-weight:800}
  .offer-band .hi{color:var(--white)}

  .contact-band{left:0;top:399px;width:738px;height:93px;background:var(--charcoal)}
  .cta{left:20px;top:9px;color:var(--white);font-weight:800;font-size:17px}
  .phone-box{left:20px;top:38px;width:262px;height:37px;border:2.5px solid var(--green);border-radius:5px;display:flex;align-items:center;gap:18px;padding-left:18px;color:var(--white);font-size:25px;font-weight:500}
  .web{display:flex;align-items:center;gap:12px;color:var(--white);font-size:15px}

  .badge{left:522px;top:279px;width:194px;height:194px}
  .badge__text{left:0;top:0;width:194px;text-align:center;color:var(--white);font-weight:800}

  .back-panel{left:0;top:0;width:437px;height:492px;background:linear-gradient(180deg,var(--blue) 0%,var(--blue-deep) 100%)}
  .about-title{left:24px;top:21px;color:var(--white);font-weight:800;font-size:18px}
  .about-rule{left:24px;top:46px;width:90px;height:2px;background:var(--green)}
  .shot{top:63px;width:187px;height:109px;box-shadow:0 2px 5px rgba(0,0,0,.4)}
  .about-copy{left:23px;top:186px;width:390px;color:var(--white);font-size:10.2px;line-height:12.4px}
  .point{left:23px;width:383px;height:30px;border:1.5px solid var(--green);border-radius:16px;display:flex;align-items:center;color:var(--white);font-size:10px;font-weight:700;text-transform:uppercase;background:linear-gradient(90deg,rgba(0,0,0,0),rgba(21,101,184,.6))}
  .point__icon{width:32px;height:32px;margin-left:-2px;border-radius:50%;background:radial-gradient(circle at 40% 35%,#8fd44a,var(--green-dark));display:flex;align-items:center;justify-content:center;flex:none}
  .point__text{margin-left:12px;line-height:12px}
  .point .hi{color:var(--green)}
  .callnow-band{left:0;top:408px;width:437px;height:63px;background:var(--charcoal)}
  .callnow{left:24px;top:5px;color:var(--green);font-weight:800;font-size:21px;line-height:27px}
  .phone-pill{left:171px;top:16px;width:241px;height:37px;border:2.5px solid var(--green);border-radius:19px;color:var(--white);font-size:22px;font-weight:500;display:flex;align-items:center;padding-left:62px}
  .phone-disc{left:-4px;top:-5px;width:42px;height:42px;border-radius:50%;background:var(--white);display:flex;align-items:center;justify-content:center}

  .stamp{left:603px;top:25px;width:111px;height:130px;background:var(--stamp)}
  .address-line{left:464px;width:250px;height:1.5px;background:#9a9a9a}
  .web--back{left:568px;top:449px;color:var(--ink);font-size:12px;gap:10px}
</style>
</head>
<body>

<section class="card card--front">
  <svg class="abs photo-house" viewBox="0 0 738 400" role="img" aria-label="Photo of a well-kept two-storey craftsman house with gabled roof and garden under a blue sky">
    <defs>
      <linearGradient id="houseTone" x1="0" y1="0" x2="0" y2="1">
        <stop offset="0" stop-color="#8fbbe6"/>
        <stop offset=".35" stop-color="#7d8673"/>
        <stop offset=".75" stop-color="#6d7462"/>
        <stop offset="1" stop-color="#6a9a3c"/>
      </linearGradient>
    </defs>
    <polygon points="370,0 738,0 738,400 240,400" fill="url(#houseTone)"/>
    <polygon points="368,0 376,0 270,334 262,334" fill="var(--green)"/>
  </svg>

  <div class="abs brand" style="left:22px;top:28px">
    <span class="brand__mark"></span><span class="brand__name">BRINDLEVALE</span>
  </div>
  <div class="abs tagline" style="left:22px;top:62px">The Smarter Approach to Pest Control</div>

  <div class="abs headline headline--green" style="left:20px;top:85px">Have You</div>
  <div class="abs headline headline--grey" style="left:19px;top:127px">Scheduled Your Annual</div>
  <div class="abs headline headline--red" style="left:19px;top:153px">Termite Inspection?</div>
  <div class="abs subhead" style="left:21px;top:191px">Don't wait. Protect your home today!</div>

  <div class="abs insects" role="img" aria-label="Illustration of a large termite with several ants around it"></div>

  <div class="abs offer-band">
    <p style="top:10px">ABSOLUTELY <b class="hi">FREE INSPECTION.</b> &nbsp;<b>NO</b> OBLIGATION.</p>
    <p style="top:29px"><b>TERMITES CAN CAUSE SEVERE DAMAGE TO YOUR HOME.</b></p>
  </div>

  <div class="abs contact-band">
    <div class="abs cta">CALL US FOR A APPOINTMENT TODAY!</div>
    <div class="abs phone-box">
      <svg width="22" height="22" viewBox="0 0 24 24"><path d="M6.6 10.8a15 15 0 0 0 6.6 6.6l2.2-2.2a1 1 0 0 1 1-.25 11.4 11.4 0 0 0 3.6.57 1 1 0 0 1 1 1V20a1 1 0 0 1-1 1A17 17 0 0 1 3 4a1 1 0 0 1 1-1h3.5a1 1 0 0 1 1 1c0 1.25.2 2.45.57 3.57a1 1 0 0 1-.25 1z" fill="var(--green)"/><path d="M14 3a7 7 0 0 1 7 7M14 6.5a3.5 3.5 0 0 1 3.5 3.5" stroke="var(--green)" stroke-width="1.8" fill="none"/></svg>
      <span>+123 456 7890</span>
    </div>
    <div class="abs web" style="left:328px;top:52px">
      <svg width="20" height="20" viewBox="0 0 24 24" fill="none" stroke="var(--green)" stroke-width="1.5"><circle cx="12" cy="12" r="10"/><ellipse cx="12" cy="12" rx="4.5" ry="10"/><path d="M2 12h20M4 7h16M4 17h16"/></svg>
      <span>www.brindlevale.com</span>
    </div>
  </div>

  <div class="abs badge">
    <svg width="194" height="194" viewBox="0 0 194 194">
      <g fill="var(--green-dark)">
        <rect x="28.4" y="28.4" width="137.2" height="137.2"/>
        <rect x="28.4" y="28.4" width="137.2" height="137.2" transform="rotate(15 97 97)"/>
        <rect x="28.4" y="28.4" width="137.2" height="137.2" transform="rotate(30 97 97)"/>
        <rect x="28.4" y="28.4" width="137.2" height="137.2" transform="rotate(45 97 97)"/>
        <rect x="28.4" y="28.4" width="137.2" height="137.2" transform="rotate(60 97 97)"/>
        <rect x="28.4" y="28.4" width="137.2" height="137.2" transform="rotate(75 97 97)"/>
      </g>
      <circle cx="97" cy="97" r="84" fill="var(--green)"/>
      <circle cx="97" cy="97" r="80" fill="none" stroke="var(--white)" stroke-width="1.2"/>
      <line x1="40" y1="132" x2="154" y2="132" stroke="var(--white)" stroke-width="1"/>
    </svg>
    <div class="abs badge__text" style="top:40px;font-size:33px;line-height:1">10%</div>
    <div class="abs badge__text" style="top:75px;font-size:21px;line-height:1">DISCOUNT</div>
    <div class="abs badge__text" style="top:98px;font-size:12px;font-weight:500;line-height:14px">ON ANY SERVICE<br>GUARANTEED</div>
    <div class="abs badge__text" style="top:137px;font-size:8.5px;font-weight:500">IF YOU CALL TODAY</div>
  </div>
</section>

<section class="card card--back">
  <div class="abs back-panel">
    <div class="abs about-title">ABOUT US</div>
    <div class="abs about-rule"></div>
    <div class="abs shot" style="left:23px;background:linear-gradient(135deg,#d9d4c8,#8a6a4a 55%,#5e4634)" role="img" aria-label="Photo of termite-damaged wooden wall framing"></div>
    <div class="abs shot" style="left:226px;background:linear-gradient(135deg,#5a4030,#7a5a40 50%,#3e2a1e)" role="img" aria-label="Photo of termites crawling on rotting wood"></div>
    <p class="abs about-copy">Lorem ipsum dolor sit amet, consectetur adipiscing elit, sed do eiusmod tempor incididunt ut labore et dolore magna aliqua. Quis ipsum suspendisse ultrices gravida. Risus commodo viverra maecenas accumsan lacus vel facilisis.</p>

    <div class="abs point" style="top:251px">
      <span class="point__icon"><svg width="16" height="16" viewBox="0 0 24 24" fill="none" stroke="#fff" stroke-width="1.8"><path d="M9 18h6M10 21h4M12 3a6 6 0 0 0-3.5 10.9V16h7v-2.1A6 6 0 0 0 12 3z"/></svg></span>
      <span class="point__text">The smarter approach to <span class="hi">pest control.</span></span>
    </div>
    <div class="abs point" style="top:302px">
      <span class="point__icon"><svg width="16" height="16" viewBox="0 0 24 24" fill="none" stroke="#fff" stroke-width="1.8"><path d="M3 11l9-7 9 7M5 10v10h5v-6h4v6h5V10"/></svg></span>
      <span class="point__text">Protect your most <span class="hi">valuable asset.</span></span>
    </div>
    <div class="abs point" style="top:354px">
      <span class="point__icon"><svg width="16" height="16" viewBox="0 0 24 24" fill="none" stroke="#fff" stroke-width="1.8"><path d="M3 12l8-8h9v9l-8 8z"/><path d="M10 15l5-5"/><circle cx="10.5" cy="10.5" r="1"/><circle cx="14.5" cy="14.5" r="1"/></svg></span>
      <span class="point__text"><span class="hi">10% discount</span> on any service guaranteed if you call<br>today.</span>
    </div>

    <div class="abs callnow-band">
      <div class="abs callnow">CALL US<br>NOW!</div>
      <div class="abs phone-pill">
        <span class="abs phone-disc"><svg width="24" height="24" viewBox="0 0 24 24"><path d="M6.6 10.8a15 15 0 0 0 6.6 6.6l2.2-2.2a1 1 0 0 1 1-.25 11.4 11.4 0 0 0 3.6.57 1 1 0 0 1 1 1V20a1 1 0 0 1-1 1A17 17 0 0 1 3 4a1 1 0 0 1 1-1h3.5a1 1 0 0 1 1 1c0 1.25.2 2.45.57 3.57a1 1 0 0 1-.25 1z" fill="var(--green)"/><path d="M14 3a7 7 0 0 1 7 7M14 6.5a3.5 3.5 0 0 1 3.5 3.5" stroke="var(--green)" stroke-width="1.8" fill="none"/></svg></span>
        +123 456 7890
      </div>
    </div>
  </div>

  <div class="abs brand" style="left:466px;top:30px;gap:6px">
    <span class="brand__mark" style="width:13px;height:13px"></span><span class="brand__name" style="font-size:13px">BRINDLEVALE</span>
  </div>
  <div class="abs stamp"></div>
  <div class="abs address-line" style="top:208px"></div>
  <div class="abs address-line" style="top:237px"></div>
  <div class="abs address-line" style="top:266px"></div>
  <div class="abs address-line" style="top:297px"></div>
  <div class="abs address-line" style="top:326px"></div>
  <div class="abs address-line" style="top:357px"></div>
  <div class="abs address-line" style="top:387px"></div>
  <div class="abs web web--back">
    <svg width="15" height="15" viewBox="0 0 24 24" fill="none" stroke="var(--green)" stroke-width="1.6"><circle cx="12" cy="12" r="10"/><ellipse cx="12" cy="12" rx="4.5" ry="10"/><path d="M2 12h20M4 7h16M4 17h16"/></svg>
    <span>www.brindlevale.com</span>
  </div>
</section>

</body>
</html>
```